Property risk and finance brokerage company needs a business card design

Tarn Financial requires a business card design. Please integrate existing logo (refer uploaded file).
hex codes used on logo #002649 #008ED6 #444F51 #ADAFAA
font used - Cinzel
Contact information
Roslyn Venterelli
Director
Mobile: 0471 385 902
email: r.venterelli@tarnfinancial.com.au
website: www.tarnfinancial.com.au
CRN : 815390
PO Box 547
Ashcombe, Victoria, 3188
Horizontal orientation please

```html
<!DOCTYPE html>
<html lang="en">
<head>
<meta charset="UTF-8">
<title>Tarn Financial – Business Card</title>
<link rel="stylesheet" href="https://fonts.googleapis.com/css2?family=Cinzel:wght@400;600&family=Questrial&family=Didact+Gothic&display=swap">
<style>
  :root {
    --navy: #002649;
    --sky: #008ed6;
    --mid-blue: #1f6fae;
    --slate: #444f51;
    --stone: #adafaa;
    --card: #f6f6f5;
    --backdrop: #e4e6e3;
    --ink: #4b4f52;
  }
  * { margin: 0; padding: 0; box-sizing: border-box; }
  html, body {
    width: 1200px;
    height: 900px;
    overflow: hidden;
    background: var(--backdrop);
  }
  .canvas {
    position: relative;
    width: 1200px;
    height: 900px;
  }
  .card {
    position: absolute;
    width: 600px;
    height: 343px;
    background: var(--card);
    box-shadow: 0 6px 18px rgba(0, 0, 0, 0.12);
    overflow: hidden;
  }
  .card--front { left: 300px; top: 70px; }
  .card--back { left: 300px; top: 473px; }

  /* Front: company name */
  .brand {
    position: absolute;
    inset: 0;
    display: flex;
    align-items: center;
    justify-content: center;
    gap: 16px;
  }
  .brand__dot {
    width: 34px;
    height: 34px;
    border-radius: 50%;
    background: var(--sky);
  }
  .brand__name {
    font-family: "Cinzel", serif;
    font-weight: 400;
    font-size: 40px;
    letter-spacing: 2px;
    color: var(--navy);
  }

  /* Back: contact block */
  .contact {
    position: absolute;
    left: 40px;
    top: 40px;
    width: 310px;
    font-family: "Didact Gothic", "Questrial", sans-serif;
    color: var(--ink);
    font-size: 12.5px;
    line-height: 1.6;
  }
  .contact__name {
    font-family: "Questrial", sans-serif;
    font-weight: 700;
    font-style: italic;
    font-size: 18px;
    color: var(--slate);
    padding-left: 110px;
  }
  .contact__role {
    font-style: italic;
    color: var(--mid-blue);
    font-size: 12px;
    padding-left: 110px;
    margin-bottom: 10px;
  }
  .contact__address { padding-left: 150px; margin-bottom: 6px; }
  .contact__line { text-align: right; white-space: nowrap; }
  .contact__label {
    font-weight: 700;
    color: var(--mid-blue);
  }
  .contact__line--rep .contact__label { color: var(--navy); }

  .swoosh {
    position: absolute;
    left: 0;
    top: 0;
    width: 600px;
    height: 343px;
  }
  .mark-echo {
    position: absolute;
    right: 80px;
    bottom: 62px;
    width: 160px;
    height: 160px;
    border-radius: 50%;
    background: radial-gradient(circle at 45% 40%, var(--sky), var(--mid-blue) 70%);
  }
</style>
</head>
<body>
<main class="canvas">
  <section class="card card--front" aria-label="Business card front">
    <div class="brand">
      <span class="brand__dot"></span>
      <span class="brand__name">Tarn Financial</span>
    </div>
  </section>

  <section class="card card--back" aria-label="Business card back">
    <svg class="swoosh" viewBox="0 0 600 343" aria-hidden="true">
      <path d="M0 250 C150 285 330 300 600 343 L0 343 Z" fill="var(--sky)" opacity="0.55"/>
      <path d="M0 262 C160 296 340 312 560 343 L0 343 Z" fill="var(--mid-blue)"/>
      <path d="M0 300 C140 320 260 332 380 343 L0 343 Z" fill="var(--card)"/>
    </svg>
    <div class="mark-echo" role="img" aria-label="Place for the company's tree emblem"></div>

    <div class="contact">
      <p class="contact__name">Roslyn Venterelli</p>
      <p class="contact__role">Managing Director</p>
      <p class="contact__address">PO Box 547<br>Ashcombe, Victoria, 3188</p>
      <p class="contact__line"><span class="contact__label">Mobile:</span> 0471 385 902</p>
      <p class="contact__line"><span class="contact__label">email:</span> r.venterelli@tarnfinancial.com.au</p>
      <p class="contact__line contact__line--rep"><span class="contact__label">Credit Rep No. :</span> nnn nnn nnn</p>
    </div>
  </section>
</main>
</body>
</html>
```